Business Card Design

We are an import/export consulting business dealing with all aspects of import/export regulations. Our current design if you look at our website (www.tavrelis.com) are different country flags. It is our business to stay up to date on laws and regulations. We assist companies worldwide. We would like to keep with the flag theme but something different or maybe someone can come up with something totally different that would capture our attention. We are open to suggestions. This design then will transfer over to letterhead, our website, marketing brochures, etc.

Industry/Entity Type

Marketing

Contact Information for Business Card

Dorothy M. Tavrelis, President
Tavrelis Global Advisors, LLC
7 Birchwood Lane,
Larkfield, VT 05291

```html
<!DOCTYPE html>
<html lang="en">
<head>
<meta charset="utf-8">
<title>Tavrelis Business Card</title>
<link rel="stylesheet" href="https://fonts.googleapis.com/css2?family=Arimo:wght@400;700&family=Oswald:wght@300&display=swap">
<style>
  :root {
    --backdrop: #d9d6d1;
    --ink-black: #151515;
    --stripe-graphite: #2f2f2c;
    --stripe-teal: #2d3c39;
    --stripe-vermilion: #e6472b;
    --stripe-peach: #e9c08c;
    --parchment: #e7d7a9;
    --map-tone: #3a3a38;
    --gold: #cfae70;
    --text-light: #e9e2cf;
  }
  * { box-sizing: border-box; margin: 0; padding: 0; }
  html, body { width: 1200px; height: 873px; overflow: hidden; }
  body {
    background: var(--backdrop);
    font-family: "Arimo", Arial, sans-serif;
    position: relative;
  }
  .card {
    position: absolute;
    top: 156px;
    width: 320px;
    height: 560px;
    background: var(--ink-black);
    overflow: hidden;
    box-shadow: 0 10px 28px rgba(0,0,0,.22);
  }
  .card--front { left: 220px; }
  .card--back { left: 660px; }

  /* front */
  .accent-band {
    position: absolute;
    left: 0; right: 0;
    top: 70px;
    height: 30px;
    background: linear-gradient(90deg, var(--stripe-vermilion) 0%, var(--stripe-peach) 100%);
  }
  .brand {
    position: absolute;
    left: 160px;
    top: 330px;
    transform: rotate(90deg);
    transform-origin: left top;
    font-family: "Oswald", "Arial Narrow", sans-serif;
    font-weight: 300;
    font-size: 26px;
    letter-spacing: 3px;
    color: var(--gold);
    white-space: nowrap;
  }

  /* back */
  .stripe {
    position: absolute;
    left: 0; right: 0;
    display: flex;
    align-items: center;
    padding-left: 34px;
    font-size: 12.5px;
    color: var(--text-light);
    letter-spacing: .2px;
    white-space: nowrap;
  }
  .stripe--name { top: 0; height: 62px; background: var(--ink-black); align-items: flex-end; padding-bottom: 14px; }
  .stripe--title { top: 62px; height: 58px; background: var(--stripe-graphite); padding-left: 52px; }
  .stripe--street { top: 120px; height: 58px; background: var(--stripe-teal); padding-left: 70px; }
  .stripe--city { top: 178px; height: 58px; background: var(--stripe-vermilion); padding-left: 88px; }
  .panel-map {
    position: absolute;
    left: 0; right: 0;
    top: 236px;
    height: 208px;
    background: var(--parchment);
  }
  .map-area {
    position: absolute;
    left: 96px;
    top: 40px;
    width: 190px;
    height: 100px;
    border-radius: 40px;
    background: radial-gradient(ellipse at center, var(--map-tone) 0%, rgba(58,58,56,.55) 60%, rgba(58,58,56,0) 100%);
  }
  .website {
    position: absolute;
    left: 0; right: 0;
    bottom: 0;
    height: 116px;
    padding: 26px 0 0 46px;
    font-weight: 700;
    font-size: 27px;
    color: var(--gold);
    letter-spacing: .5px;
  }
</style>
</head>
<body>
  <section class="card card--front" aria-label="Card front">
    <div class="accent-band" role="img" aria-label="Colour band with a row of small triangles"></div>
    <div class="brand">TAVRELIS</div>
  </section>

  <section class="card card--back" aria-label="Card back">
    <div class="stripe stripe--name">Dorothy M. Tavrelis</div>
    <div class="stripe stripe--title">President Tavrelis Global Advisors,</div>
    <div class="stripe stripe--street">LLC 7 Birchwood Lane</div>
    <div class="stripe stripe--city">Larkfield, VT 05291</div>
    <div class="panel-map">
      <div class="map-area" role="img" aria-label="World map with a marker on the eastern United States"></div>
    </div>
    <div class="website">tavrelis.com</div>
  </section>
</body>
</html>
```